Renewable energy company needs modern memorable marketing brochure

We have an 8 page marketing brochure which was created in house. This needs to be revamped and modernised to stand out from our competitors in Australia, Chile and the UK. The brochure should depict us as a professional and dynamic company and instil confidence in prospective clients that we do a professional job. Once the design is finalised we will need a country specific document in the correct language i.e. Spanish for Chile. We are happy to pay for these iterations. We have a company logo which we would like incorporated into the brochure and the colours from the logo utilised where appropriate in the overall design. I have uploaded our existing brochure for an example of the content that the brochure needs to have and can upload the images separately if they are needed. Images in the brochure need to be copyright free and we have lots of photos in-house. I have added all the images from the last brochure and also the text in Indesign so it can be copied easily if needed.

Target Market(s)

landowners and companies

Industry/Entity Type

It Company

Requirements
Must have
• A clean modern look with some colours taken from the logo colour. Be easy to print in various countries.

```html
<!DOCTYPE html>
<html lang="en">
<head>
<meta charset="utf-8">
<title>Solvane Energy – Brochure Spread</title>
<link href="https://fonts.googleapis.com/css2?family=Open+Sans:wght@400;600;700&family=Montserrat:wght@700&display=swap" rel="stylesheet">
<style>
  :root{
    --teal:#1aa58e;
    --teal-dark:#138a76;
    --ink:#3a3a3a;
    --ink-soft:#555;
    --page:#f1f1f1;
    --bg:#dfe3e6;
    --panel:rgba(240,240,240,.93);
  }
  *{box-sizing:border-box;margin:0;padding:0}
  html,body{width:1200px;height:1200px;overflow:hidden;background:var(--bg);font-family:"Open Sans",sans-serif;color:var(--ink)}
  .spread{position:absolute;left:40px;top:206px;width:1120px;height:788px;background:var(--page);box-shadow:0 6px 24px rgba(0,0,0,.18)}
  .photo{position:absolute;left:0;top:0;width:563px;height:788px;
    background:linear-gradient(180deg,#b9d3ea 0%,#9fbf6a 18%,#6f9a3a 45%,#5c7a3a 62%,#7f8e84 75%,#5d6d62 92%,#8a7a5e 100%)}
  .about{position:absolute;left:0;top:108px;width:274px;height:366px;background:var(--panel);border-radius:0 14px 14px 0;padding:0 14px 0 13px}
  .about-title{margin:14px -14px 12px -13px;width:256px;height:46px;background:var(--teal);color:#fff;font-family:"Montserrat",sans-serif;font-weight:700;font-size:20px;display:flex;align-items:center;justify-content:center}
  .about p{font-size:10.6px;line-height:13px;text-align:justify;color:var(--ink-soft);margin-bottom:8px}
  .content{position:absolute;left:587px;top:0;width:510px}
  .heading{position:absolute;left:0;font-size:29px;color:var(--teal);font-weight:400;letter-spacing:-.3px;white-space:nowrap}
  .heading strong{font-weight:700}
  .subhead{position:absolute;left:0;top:65px;font-size:19px;color:var(--ink);white-space:nowrap}
  .lede{position:absolute;left:0;top:98px;width:510px;font-size:11.6px;line-height:19.2px;text-align:justify;color:var(--ink-soft)}
  .services{position:absolute;top:242px;left:0;width:510px;height:120px}
  .service{position:absolute;width:120px;margin-left:-60px;text-align:center}
  .service svg{display:block;margin:0 auto}
  .service span{display:block;margin-top:8px;font-size:11.6px;line-height:15px;color:var(--teal)}
  .offer-lead{position:absolute;left:0;top:454px;font-size:15px;line-height:20px;color:var(--ink);text-transform:uppercase}
  .offer-note{position:absolute;left:0;top:523px;font-size:11px;color:var(--ink-soft)}
  .promises{position:absolute;left:28px;top:556px;list-style:none}
  .promises li{height:39.2px;display:flex;align-items:center;font-size:11.4px;color:var(--ink-soft)}
  .promises svg{width:18px;height:18px;margin-right:12px;flex:none}
</style>
</head>
<body>
<div class="spread">
  <div class="photo" role="img" aria-label="Photo of a large oak tree in a green field behind rows of ground-mounted solar panels under a blue sky"></div>

  <section class="about">
    <h2 class="about-title">ABOUT US</h2>
    <p>Solvane Energy is a solar development company that is at the forefront of the global energy revolution.</p>
    <p>We work in an industry that is rapidly changing: Growing environmental consciousness coupled with the rapidly declining cost of renewables is powering the switch away from dirty fossil fuels and onto clean energy.</p>
    <p>Solvane Energy is intent on facilitating this transformation.</p>
    <p>Delivering clean, cheap and reliable electricity is our goal, and we see the sun as the obvious source. Solar farms provide cost-effective, low impact energy that directly benefits local communities and indigenous wildlife.</p>
    <p>With development partners on four continents, Solvane Energy has global outreach and a network of solar experts.</p>
  </section>

  <section class="content">
    <h1 class="heading" style="top:26px"><strong>WHAT</strong> WE DO?</h1>
    <h3 class="subhead">SOLVANE ENERGY DEVELOPS SOLAR PROJECTS</h3>
    <p class="lede">We guide the project from inception through to its commissioning. This entails finding a suitable site, negotiating a lease on the land with the landowner, and taking the project through the necessary Development Approval hurdles. We also consult with the Network Service Provider and deal with any connection criteria. To ensure the project is of maximum benefit to the local community and wildlife, we also conduct various environmental and community impact assessments.</p>

    <div class="services">
      <div class="service" style="left:71px">
        <svg width="80" height="84" viewBox="0 0 80 84"><ellipse cx="40" cy="81" rx="26" ry="2" fill="#ccc"/><circle cx="40" cy="38" r="38" fill="var(--teal)"/>
          <g fill="#fff"><circle cx="34" cy="44" r="9"/><circle cx="49" cy="30" r="6"/>
          <g stroke="#fff" stroke-width="5"><path d="M34 31v26M21 44h26M25 35l18 18M43 35l-18 18"/><path d="M49 22v16M41 30h16M43 24l12 12M55 24l-12 12" stroke-width="3.5"/></g></g>
          <circle cx="34" cy="44" r="3.5" fill="var(--teal)"/><circle cx="49" cy="30" r="2.5" fill="var(--teal)"/></svg>
        <span>Development</span>
      </div>
      <div class="service" style="left:190px">
        <svg width="80" height="84" viewBox="0 0 80 84"><ellipse cx="40" cy="81" rx="26" ry="2" fill="#ccc"/><circle cx="40" cy="38" r="38" fill="var(--teal)"/>
          <g fill="none" stroke="#fff" stroke-width="2.2"><path d="M20 40c0-9 8-15 18-15 7 0 12 3 15 7l5 1v8l-5 2-3 5v4h-5v-3h-10v3h-5v-5c-6-2-10-4-10-7z"/><path d="M30 22a6 6 0 0 1 12 0" stroke-dasharray="2 2"/></g>
          <rect x="47" y="44" width="12" height="10" rx="1.5" fill="#fff"/><path d="M49.5 44v-3a3.5 3.5 0 0 1 7 0v3" fill="none" stroke="#fff" stroke-width="2"/></svg>
        <span>Capital</span>
      </div>
      <div class="service" style="left:312px">
        <svg width="80" height="84" viewBox="0 0 80 84"><ellipse cx="40" cy="81" rx="26" ry="2" fill="#ccc"/><circle cx="40" cy="38" r="38" fill="var(--teal)"/>
          <g fill="none" stroke="#fff" stroke-width="2.4"><rect x="23" y="20" width="30" height="36" rx="2"/><path d="M28 29h4M35 29h13M28 36h4M35 36h13M28 43h4M35 43h9"/></g>
          <path d="M46 54l12-14 4 3-12 14-5 1z" fill="#fff"/></svg>
        <span>Project Management</span>
      </div>
      <div class="service" style="left:434px">
        <svg width="80" height="84" viewBox="0 0 80 84"><ellipse cx="40" cy="81" rx="26" ry="2" fill="#ccc"/><circle cx="40" cy="38" r="38" fill="var(--teal)"/>
          <g stroke="#fff" stroke-width="2.4"><path d="M40 38L26 22M40 38L56 24M40 38L24 48M40 38L52 56M40 38V16"/></g>
          <g fill="#fff"><circle cx="40" cy="38" r="8"/><circle cx="26" cy="22" r="5"/><circle cx="56" cy="24" r="5"/><circle cx="24" cy="48" r="5"/><circle cx="52" cy="56" r="5"/><circle cx="40" cy="16" r="3.5"/></g></svg>
        <span>Operations and<br>Maintenance</span>
      </div>
    </div>

    <h1 class="heading" style="top:411px"><strong>WHAT</strong> WE OFFER?</h1>
    <p class="offer-lead">In leasing your land for a solar project, you will receive<br>a generous fixed annual rental income paid on a per hectare<br>basis for the duration of the project’s lifetime.</p>
    <p class="offer-note">Solvane Energy runs a streamline process from initial contact through to installation.</p>

    <ul class="promises">
      <li><svg viewBox="0 0 18 18"><g stroke="#333" stroke-width="1.4"><path d="M9 9L3 4M9 9l6-4M9 9l-6 5M9 9l5 6M9 9V2"/></g><g fill="#333"><circle cx="9" cy="9" r="2.8"/><circle cx="3" cy="4" r="1.8"/><circle cx="15" cy="5" r="1.8"/><circle cx="3" cy="14" r="1.8"/><circle cx="14" cy="15" r="1.8"/></g></svg>We will organise all of the development and grid connection processes</li>
      <li><svg viewBox="0 0 18 18"><path d="M6 2h6l-1 3 3 10H4L7 5z" fill="#333"/></svg>We will pay for all associated legal costs</li>
      <li><svg viewBox="0 0 18 18"><path d="M7 2h4l-1 3c3 1 5 4 5 7 0 3-2 4-6 4s-6-1-6-4c0-3 2-6 5-7z" fill="#333"/><text x="9" y="14" font-size="7" font-family="Open Sans,sans-serif" font-weight="700" fill="#fff" text-anchor="middle">$</text></svg>We will provide all of the funding for the project</li>
      <li><svg viewBox="0 0 18 18"><g fill="#333"><path d="M4 7a5 5 0 0 1 10 0z"/><circle cx="9" cy="8.5" r="3"/><path d="M2 17c0-4 3-6 7-6s7 2 7 6z"/></g></svg>We will orchestrate the construction</li>
      <li><svg viewBox="0 0 18 18"><g fill="none" stroke="#333" stroke-width="1.8"><path d="M14 7a5.5 5.5 0 0 0-10-1M4 11a5.5 5.5 0 0 0 10 1"/></g><path d="M3 2v5h5zM15 16v-5h-5z" fill="#333"/></svg>We ensure that after the lease the land will be restored to its original condition</li>
    </ul>
  </section>
</div>
</body>
</html>
```